Visitenkarten für ein Metallverarbeitsungsbetrieb
Zielgruppe
Metallverarbeitsungsbetrieb
spezialisiert auf Lasern
Aufgabenstellung
Passend zu unseren Logo und in den Farben, schlicht dennoch besonders

```html
<!DOCTYPE html>
<html lang="de">
<head>
<meta charset="utf-8">
<title>Visitenkarte – Ferrolux Metallverarbeitung</title>
<link rel="stylesheet" href="https://fonts.googleapis.com/css2?family=Open+Sans:wght@400;600;700&display=swap">
<style>
  :root {
    --backdrop: #d9dbde;
    --card: #f7f8fa;
    --ink: #2b3440;
    --ink-soft: #4a5563;
    --brand-blue: #2f8fe0;
    --brand-blue-light: #5aaaf0;
    --brand-navy: #1d4f86;
    --photo-dark: #243447;
    --photo-mid: #3f5d78;
    --spark: #f2a54a;
  }
  * { box-sizing: border-box; margin: 0; padding: 0; }
  html, body {
    width: 1200px;
    height: 800px;
    overflow: hidden;
    background: var(--backdrop);
    font-family: "Open Sans", Arial, sans-serif;
  }
  .canvas {
    width: 1200px;
    height: 800px;
    display: flex;
    align-items: center;
    justify-content: center;
  }
  .business-card {
    position: relative;
    width: 840px;
    height: 480px;
    background: var(--card);
    overflow: hidden;
    box-shadow: 0 10px 30px rgba(0,0,0,0.18);
  }
  .header-graphic {
    position: absolute;
    inset: 0;
    width: 840px;
    height: 480px;
  }
  .identity {
    position: absolute;
    left: 64px;
    top: 176px;
  }
  .person-name {
    font-size: 34px;
    font-weight: 700;
    color: var(--ink);
    line-height: 1.1;
  }
  .person-role {
    font-size: 19px;
    font-weight: 400;
    color: var(--brand-blue);
    margin-top: 4px;
  }
  .role-rule {
    width: 64px;
    height: 3px;
    background: var(--brand-blue);
    margin-top: 10px;
  }
  .contact-list {
    position: absolute;
    left: 64px;
    top: 292px;
    list-style: none;
  }
  .contact-item {
    display: flex;
    align-items: flex-start;
    gap: 14px;
    font-size: 17px;
    color: var(--ink-soft);
    line-height: 22px;
    margin-bottom: 12px;
  }
  .contact-icon {
    flex: none;
    width: 24px;
    height: 24px;
  }
</style>
</head>
<body>
<main class="canvas">
  <section class="business-card">
    <svg class="header-graphic" viewBox="0 0 840 480" aria-hidden="false">
      <defs>
        <linearGradient id="photoTone" x1="0" y1="0" x2="1" y2="1">
          <stop offset="0" stop-color="var(--photo-mid)"/>
          <stop offset="0.55" stop-color="var(--photo-dark)"/>
          <stop offset="1" stop-color="#1a2330"/>
        </linearGradient>
        <radialGradient id="sparkGlow" cx="0.55" cy="0.55" r="0.45">
          <stop offset="0" stop-color="var(--spark)" stop-opacity="0.85"/>
          <stop offset="1" stop-color="var(--spark)" stop-opacity="0"/>
        </radialGradient>
      </defs>
      <polygon class="accent-band-light" points="392,0 470,0 412,150 372,92" fill="var(--brand-blue-light)"/>
      <polygon class="accent-band-navy" points="372,92 412,150 520,310 840,310 840,340 500,340" fill="var(--brand-navy)"/>
      <g role="img" aria-label="Foto: Funkenflug bei der Metallbearbeitung">
        <polygon points="470,0 840,0 840,310 520,310 412,150" fill="url(#photoTone)"/>
        <polygon points="470,0 840,0 840,310 520,310 412,150" fill="url(#sparkGlow)"/>
      </g>
    </svg>

    <div class="identity">
      <h1 class="person-name">John Doe</h1>
      <p class="person-role">Chief Executive Officer</p>
      <div class="role-rule"></div>
    </div>

    <ul class="contact-list">
      <li class="contact-item">
        <svg class="contact-icon" viewBox="0 0 24 24"><circle cx="12" cy="12" r="12" fill="var(--brand-blue)"/><path d="M8.5 6.5l2 2-1 1.5c.8 1.6 2 2.8 3.5 3.5l1.5-1 2 2-1.3 1.8c-3.5-.5-7.5-4.5-8-8z" fill="#fff"/></svg>
        <span>+123-456-7890</span>
      </li>
      <li class="contact-item">
        <svg class="contact-icon" viewBox="0 0 24 24"><circle cx="12" cy="12" r="12" fill="var(--brand-blue)"/><rect x="6.5" y="8" width="11" height="8" rx="1" fill="#fff"/><path d="M6.8 8.5l5.2 4 5.2-4" fill="none" stroke="var(--brand-blue)" stroke-width="1.2"/></svg>
        <span>kontakt@ferrolux.de</span>
      </li>
      <li class="contact-item">
        <svg class="contact-icon" viewBox="0 0 24 24"><circle cx="12" cy="12" r="12" fill="var(--brand-blue)"/><circle cx="12" cy="12" r="5.5" fill="none" stroke="#fff" stroke-width="1.4"/><path d="M6.5 12h11M12 6.5c-2.5 3-2.5 8 0 11M12 6.5c2.5 3 2.5 8 0 11" fill="none" stroke="#fff" stroke-width="1.1"/></svg>
        <span>www.ferrolux.de</span>
      </li>
      <li class="contact-item">
        <svg class="contact-icon" viewBox="0 0 24 24"><circle cx="12" cy="12" r="12" fill="var(--brand-blue)"/><path d="M12 18s-4.5-4.6-4.5-7.5a4.5 4.5 0 0 1 9 0C16.5 13.4 12 18 12 18z" fill="#fff"/><circle cx="12" cy="10.5" r="1.6" fill="var(--brand-blue)"/></svg>
        <span>123 Anywhere St., Any<br>City, ST 12345</span>
      </li>
    </ul>
  </section>
</main>
</body>
</html>
```